Pest Control Company needs business card!

Hi there, we need a business card designed for our new Pest Control Company. Ideally this card will be simple, yet feel elegant and high end. We want to use the colours Orange, Black and White. Please see our attached logo for the exact colours.

Business card details:

Phone - 0438 517 264
Name - Gus Halloran
Email - Info@trueguardpest.com.au

We would also like to include the following list with dot points:

SERVICES / INSPECTIONS

Termites, Wood Borers, Ants, Cockroaches, Spiders, Fleas, Mice, Rats, Bed Bugs, & More!

```html
<!DOCTYPE html>
<html lang="en">
<head>
<meta charset="utf-8">
<title>Trueguard Pest Control – Business Card</title>
<link href="https://fonts.googleapis.com/css2?family=Montserrat:wght@400;500;600;800&display=swap" rel="stylesheet">
<style>
  :root {
    --red: #e3202e;
    --ink: #1d1d1f;
    --card-dark: #222224;
    --white: #ffffff;
    --grey-text: #3a3a3c;
    --stage: #e9e9eb;
  }
  * { box-sizing: border-box; margin: 0; padding: 0; }
  html, body {
    width: 1200px; height: 912px; overflow: hidden;
    background: var(--stage);
    font-family: "Montserrat", sans-serif;
  }
  .stage {
    width: 1200px; height: 912px;
    display: flex; flex-direction: column;
    align-items: center; justify-content: center; gap: 48px;
  }
  .card {
    position: relative;
    width: 680px; height: 388px;
    border-radius: 22px;
    overflow: hidden;
    box-shadow: 0 10px 30px rgba(0,0,0,0.18);
  }
  /* Front */
  .card--front {
    background: var(--card-dark);
    color: var(--white);
    display: flex; flex-direction: column;
    align-items: center; justify-content: center;
    text-align: center;
  }
  .brand {
    display: flex; align-items: center; gap: 14px;
    font-weight: 800; text-transform: uppercase;
    letter-spacing: 0.5px; line-height: 1;
  }
  .brand__dot {
    width: 22px; height: 22px; border-radius: 50%;
    background: var(--red); flex: none;
  }
  .card--front .brand { font-size: 40px; color: var(--white); margin-bottom: 40px; }
  .services__title {
    color: var(--red); font-weight: 500; font-size: 24px;
    letter-spacing: 1px; margin-bottom: 14px;
  }
  .services__list {
    font-size: 17px; font-weight: 400; letter-spacing: 0.6px;
    line-height: 1.55; text-transform: uppercase;
  }
  .sep { color: var(--red); margin: 0 6px; }

  /* Back */
  .card--back { background: var(--white); }
  .card--back .brand {
    position: absolute; left: 56px; top: 168px;
    font-size: 30px; color: var(--ink);
  }
  .divider {
    position: absolute; left: 382px; top: 110px;
    width: 2px; height: 128px; background: var(--red);
  }
  .contact {
    position: absolute; left: 410px; top: 112px;
    color: var(--grey-text);
  }
  .contact__name {
    color: var(--red); font-weight: 600; font-size: 26px;
    text-transform: uppercase; letter-spacing: 0.6px;
  }
  .contact__role { font-size: 18px; margin: 4px 0 18px; }
  .contact__line {
    display: flex; align-items: center; gap: 10px;
    font-size: 17px; margin-bottom: 6px;
  }
  .contact__line svg { width: 14px; height: 14px; flex: none; }
  .base-band {
    position: absolute; left: 0; bottom: 0;
    width: 680px; height: 110px;
  }
</style>
</head>
<body>
<main class="stage">

  <section class="card card--front" aria-label="Business card front">
    <div class="brand"><span class="brand__dot"></span>Trueguard Pest Control</div>
    <h2 class="services__title">SERVICES / INSPECTIONS</h2>
    <p class="services__list">
      Termites<span class="sep">|</span>Wood Borers<span class="sep">|</span>Ants<span class="sep">|</span>Cockroaches<br>
      Spiders<span class="sep">|</span>Fleas<span class="sep">|</span>Mice<span class="sep">|</span>Rats<span class="sep">|</span>Bed Bugs<span class="sep">|</span>&amp; More!
    </p>
  </section>

  <section class="card card--back" aria-label="Business card back">
    <div class="brand"><span class="brand__dot"></span>Trueguard<br>Pest Control</div>
    <div class="divider"></div>
    <div class="contact">
      <h1 class="contact__name">Gus Halloran</h1>
      <p class="contact__role">Director</p>
      <p class="contact__line">
        <svg viewBox="0 0 24 24" aria-hidden="true"><path fill="#e3202e" d="M6.6 10.8a15 15 0 0 0 6.6 6.6l2.2-2.2a1 1 0 0 1 1-.25 11.4 11.4 0 0 0 3.6.57 1 1 0 0 1 1 1V20a1 1 0 0 1-1 1A17 17 0 0 1 3 4a1 1 0 0 1 1-1h3.5a1 1 0 0 1 1 1c0 1.25.2 2.45.57 3.57a1 1 0 0 1-.25 1z"/></svg>
        0438 517 264
      </p>
      <p class="contact__line">
        <svg viewBox="0 0 24 24" aria-hidden="true"><rect x="2.5" y="5" width="19" height="14" rx="1.5" fill="none" stroke="#e3202e" stroke-width="2.2"/><path d="M3 6l9 7 9-7" fill="none" stroke="#e3202e" stroke-width="2.2"/></svg>
        Info@trueguardpest.com.au
      </p>
    </div>
    <svg class="base-band" viewBox="0 0 680 110" preserveAspectRatio="none" aria-hidden="true">
      <polygon points="0,104 470,104 490,60 680,60 680,110 0,110" fill="var(--ink)"/>
      <polygon points="0,96 462,96 482,52 495,52 475,104 0,104" fill="var(--red)"/>
    </svg>
  </section>

</main>
</body>
</html>
```